Internet of Things integrator needs logo and website design

We need a logo and website design for our company ("Vantor Grid"). We integrate IoT(Internet of Things) projects including: devices, network and sw solutions for all type of vertical markets. The image should be professional like the following site: quellan.io clear and easy surfing, and should include about the same sections shown in that website (Why Us?, Products, Resources, Company, etc). Website colors should follow logo colors (logo has to be designed and aproved first). The logo should be something like the one used at strevanhub.com (image attached), where we could use the logo to susbtitute the letter "o" in "IoT". The final design should communicate professionalism and experience.

Coding

Coded - Design and coding required

Number of Pages Required

5+ page

Font styles to use
Other font styles liked:
• see quellan.io wensite

Requirements
Must have
• Serious and professional look and feel as in: quellan.io website.
The following pages should be included:
- home page
- Why Us?
- Products
- Resources
- Company
- Newsroom
- Contact
Nice to have
• High tech look and feel
Should not have
• Fun or not serious images (cartoons, etc.)

```html
<!DOCTYPE html>
<html lang="en">
<head>
<meta charset="utf-8">
<title>Vantor Grid — Contact</title>
<link rel="stylesheet" href="https://fonts.googleapis.com/css2?family=Poppins:wght@400;500;600;700&family=Montserrat:wght@400;500;600&display=swap">
<style>
:root{
  --teal-light:#2d8b9b;
  --teal-dark:#0d3a52;
  --accent:#1fa9c9;
  --ink:#0b0b0b;
  --white:#ffffff;
  --field:#f1f1f1;
  --footer:#17191d;
  --footer-line:#2c2f35;
  --bottom:#000000;
  --muted:#c9cbd0;
}
*{margin:0;padding:0;box-sizing:border-box}
html,body{width:1036px;height:1200px;overflow:hidden;background:var(--white)}
body{position:relative;font-family:"Poppins",sans-serif;color:var(--ink)}
.abs{position:absolute}

/* Hero */
.hero{left:0;top:0;width:1036px;height:340px;
  background:radial-gradient(ellipse at 60% 45%,#1d6f82 0%,transparent 60%),
  linear-gradient(100deg,var(--teal-light) 0%,#1c6a80 40%,var(--teal-dark) 75%,#1b6d82 100%)}
.brand{font-family:"Poppins",sans-serif;font-weight:500;color:var(--white);font-size:24px;letter-spacing:.2px;white-space:nowrap}
.hero .brand{left:203px;top:24px}
.nav{top:36px;left:392px;display:flex;gap:0;font-weight:600;font-size:7.6px;letter-spacing:.5px;color:var(--white)}
.nav span{position:absolute;white-space:nowrap}
.nav-cta{left:767px;top:27px;width:67px;height:29px;background:var(--white);color:var(--ink);
  font-weight:600;font-size:7.6px;letter-spacing:.5px;display:flex;align-items:center;justify-content:center}
.hero-kicker{left:0;width:1036px;top:148px;text-align:center;color:var(--white);font-weight:700;font-size:9.5px}
.hero-title{left:0;width:1036px;top:166px;text-align:center;color:var(--white);font-weight:700;
  font-size:22.5px;line-height:26px;letter-spacing:2.6px}

/* Form section */
.section-title{left:0;width:1036px;top:385px;text-align:center;font-weight:700;font-size:22px;letter-spacing:3.2px}
.intro{left:250px;width:536px;top:424px;text-align:center;font-size:9.3px;line-height:16.3px}
.field{background:var(--field);border-radius:2px;font-size:7.6px;letter-spacing:.5px;padding-left:14px;display:flex;align-items:center}
.field.msg{align-items:flex-start;padding-top:16px}
.caret{position:absolute;right:16px;top:17px}
.submit{left:464px;top:816px;width:108px;height:39px;background:var(--ink);color:var(--white);
  font-weight:700;font-size:8.5px;letter-spacing:.6px;display:flex;align-items:center;justify-content:center}

/* Footer */
.footer{left:0;top:919px;width:1036px;height:243px;background:var(--footer)}
.divider{top:919px;width:1px;height:243px;background:var(--footer-line)}
.footer .brand{font-size:30px}
.about{left:203px;top:1012px;width:205px;font-family:"Montserrat",sans-serif;font-size:8.3px;line-height:13px;color:var(--white)}
.social{top:1081px;width:21px;height:21px;border:1px solid var(--accent);border-radius:50%}
.col-title{font-family:"Montserrat",sans-serif;font-weight:600;font-size:11px;color:var(--white);white-space:nowrap}
.col-rule{width:16px;height:1.5px;background:var(--white)}
.links{font-family:"Montserrat",sans-serif;font-size:8.5px;line-height:17.3px;color:var(--white);list-style:none}
.map{left:645px;top:995px;width:200px;height:130px;border-radius:50%;
  background:radial-gradient(ellipse,rgba(60,70,85,.45) 0%,rgba(23,25,29,0) 70%)}
.contact-line{font-family:"Montserrat",sans-serif;font-size:8.6px;line-height:13px;color:var(--white);white-space:nowrap}
.bottom{left:0;top:1162px;width:1036px;height:38px;background:var(--bottom)}
.legal{font-family:"Montserrat",sans-serif;font-size:7.4px;color:var(--muted);top:1177px;white-space:nowrap}
</style>
</head>
<body>

<header>
  <div class="abs hero" role="img" aria-label="Teal hero photo of a profile silhouette overlaid with a connected network mesh and IoT icons"></div>
  <div class="abs brand">Vantor Grid</div>
  <nav class="abs nav">
    <span style="left:0">HOME</span>
    <span style="left:46px">WHY US?</span>
    <span style="left:107px">PRODUCTS</span>
    <span style="left:175px">RESOURCES</span>
    <span style="left:247px">COMPANY</span>
    <span style="left:311px">NEWSROOM</span>
  </nav>
  <div class="abs nav-cta">CONTACT</div>
  <p class="abs hero-kicker">GET STARTED</p>
  <h1 class="abs hero-title">CONTACT US TO START YOUR DIGITAL<br>TRANSFORMATION TODAY</h1>
</header>

<main>
  <h2 class="abs section-title">GET STARTED</h2>
  <p class="abs intro">Working with Quellan is fast and easy, we can help any industrial company derive value from the edge immediately for improved operational efficiency. Contact us to start your digital transformation today.</p>

  <div class="abs field" style="left:256px;top:486px;width:254px;height:39px">FIRST NAME</div>
  <div class="abs field" style="left:527px;top:486px;width:253px;height:39px">LAST NAME</div>
  <div class="abs field" style="left:256px;top:543px;width:254px;height:39px">TITLE</div>
  <div class="abs field" style="left:527px;top:543px;width:253px;height:39px">COMPANY NAME</div>
  <div class="abs field" style="left:256px;top:600px;width:254px;height:39px">COMPANY EMAIL</div>
  <div class="abs field" style="left:527px;top:600px;width:253px;height:39px">COMPANY PHONE</div>
  <div class="abs field" style="left:256px;top:657px;width:524px;height:39px">UNITED STATES OF AMERICA (USA)
    <svg class="caret" width="8" height="5" viewBox="0 0 8 5"><path d="M0 0H8L4 5Z" fill="#0b0b0b"/></svg>
  </div>
  <div class="abs field msg" style="left:256px;top:715px;width:524px;height:80px">MESSAGE</div>
  <div class="abs submit">SUBMIT</div>
</main>

<footer>
  <div class="abs footer"></div>
  <div class="abs divider" style="left:423px"></div>
  <div class="abs divider" style="left:545px"></div>
  <div class="abs divider" style="left:678px"></div>

  <div class="abs brand" style="left:203px;top:956px;font-size:30px">Vantor Grid</div>
  <p class="abs about">Lorem ipsum dolor sit amet, consectetur adipiscing elit. Quisque iaculis elementum eleifend. Cras malesuada vitae enim id imperdiet. Vestibulum vestibulum egestas.</p>
  <div class="abs social" style="left:203px"></div>
  <div class="abs social" style="left:230px"></div>
  <div class="abs social" style="left:257px"></div>
  <div class="abs social" style="left:284px"></div>

  <div class="abs col-title" style="left:448px;top:964px">QUICK LINKS</div>
  <div class="abs col-rule" style="left:449px;top:984px"></div>
  <ul class="abs links" style="left:449px;top:1002px">
    <li>Home</li><li>Why Us?</li><li>Products</li><li>Resources</li><li>Company</li><li>Newsroom</li><li>Contact</li>
  </ul>

  <div class="abs col-title" style="left:572px;top:964px">INFORMATION</div>
  <div class="abs col-rule" style="left:573px;top:984px"></div>
  <ul class="abs links" style="left:573px;top:1002px">
    <li>Cloud</li><li>Big Data</li><li>Applications</li><li>Sensors</li><li>Robotic Systems</li><li>PLC</li>
  </ul>

  <div class="abs map" role="img" aria-label="Faint dotted world map backdrop"></div>
  <div class="abs col-title" style="left:704px;top:961px">CONTACTS</div>
  <div class="abs col-rule" style="left:705px;top:981px"></div>

  <svg class="abs" style="left:705px;top:1003px" width="7" height="7" viewBox="0 0 24 24"><path d="M6.6 10.8a15 15 0 0 0 6.6 6.6l2.2-2.2a1 1 0 0 1 1-.25 11.4 11.4 0 0 0 3.6.6 1 1 0 0 1 1 1V20a1 1 0 0 1-1 1A17 17 0 0 1 3 4a1 1 0 0 1 1-1h3.5a1 1 0 0 1 1 1 11.4 11.4 0 0 0 .6 3.6 1 1 0 0 1-.25 1z" fill="#1fa9c9"/></svg>
  <div class="abs contact-line" style="left:718px;top:1002px">+00 555 018 204</div>

  <svg class="abs" style="left:705px;top:1023px" width="7" height="6" viewBox="0 0 24 18"><path d="M0 0h24v3L12 10 0 3zM0 6l12 7 12-7v12H0z" fill="#1fa9c9"/></svg>
  <div class="abs contact-line" style="left:718px;top:1021px">hello@vantorgrid.com</div>

  <svg class="abs" style="left:705px;top:1040px" width="6" height="8" viewBox="0 0 12 16"><path d="M6 0a6 6 0 0 0-6 6c0 4.5 6 10 6 10s6-5.5 6-10a6 6 0 0 0-6-6zm0 8.5A2.5 2.5 0 1 1 6 3.5a2.5 2.5 0 0 1 0 5z" fill="#1fa9c9"/></svg>
  <div class="abs contact-line" style="left:718px;top:1040px">PO Box 40218 Harlow st. 112,<br>Fairmont, Ohio, Us.</div>

  <div class="abs bottom"></div>
  <div class="abs legal" style="left:204px">© Copyright 2020 Vantor Grid. All Rights Reserved.</div>
  <div class="abs legal" style="left:706px">Privacy Policy &nbsp;&nbsp;|&nbsp;&nbsp; Terms &amp; Conditions</div>
</footer>

</body>
</html>
```